Fernvale Business Card Design

We are looking for a fresh business card design for our new logo. We would like a business card that is unique but friendly. We are in the window coverings business offering blinds, shutters and shades for homes.

Target Market(s)

Targeting the end-consumer

Industry/Entity Type

Business

Requirements
Must have
• Must have a dedicates space for a photo of our sales person. Must contain our new logo (attached).

```html
<!DOCTYPE html>
<html lang="en">
<head>
<meta charset="utf-8">
<title>Fernvale Business Card</title>
<link href="https://fonts.googleapis.com/css2?family=Lato:wght@400;700&display=swap" rel="stylesheet">
<style>
  :root {
    --stage: #1f1f20;
    --card-grey: #646568;
    --card-white: #ffffff;
    --ink: #5f6062;
    --green: #8cc63f;
    --photo-a: #e9ecef;
    --photo-b: #2d3a55;
  }
  * { box-sizing: border-box; margin: 0; padding: 0; }
  html, body { width: 1189px; height: 1200px; overflow: hidden; background: var(--stage); }
  body { position: relative; font-family: "Lato", sans-serif; }

  .card { position: absolute; left: 170px; width: 857px; height: 489px; overflow: hidden; }
  .card-front { top: 68px; background: var(--card-grey); border-top-right-radius: 80px; }
  .card-back { top: 625px; background: var(--card-white); border-top-left-radius: 80px; }

  .brand { position: absolute; display: flex; align-items: center; gap: 20px; }
  .brand-mark { width: 64px; height: 64px; background: var(--green); }
  .brand-name { font-size: 74px; font-weight: 400; line-height: 1; letter-spacing: 0.5px; }
  .card-front .brand { left: 356px; top: 343px; }
  .card-front .brand-name { color: #ffffff; }
  .card-back .brand { left: 43px; top: 73px; }
  .card-back .brand-name { color: var(--ink); }

  .photo-frame {
    position: absolute; left: 625px; top: 42px; width: 189px; height: 189px;
    border: 10px solid var(--green); border-bottom-right-radius: 52px;
    background: linear-gradient(180deg, var(--photo-a) 0%, var(--photo-a) 55%, var(--photo-b) 100%);
  }

  .person { position: absolute; left: 43px; top: 277px; }
  .person-name { font-size: 28px; font-weight: 700; color: var(--ink); line-height: 28px; }
  .person-role { font-size: 21px; color: var(--green); line-height: 22px; }
  .divider { position: absolute; left: 43px; top: 332px; width: 771px; height: 1px; background: var(--green); }

  .contacts { position: absolute; left: 43px; top: 358px; list-style: none; }
  .contact { display: flex; align-items: center; height: 28.5px; font-size: 22px; color: var(--ink); }
  .contact svg { width: 26px; height: 26px; margin-right: 16px; flex: none; }

  .address { position: absolute; right: 43px; top: 388px; text-align: right; font-size: 22px; line-height: 27px; color: var(--ink); font-style: normal; }
</style>
</head>
<body>
  <section class="card card-front">
    <div class="brand">
      <span class="brand-mark"></span>
      <span class="brand-name">Fernvale</span>
    </div>
  </section>

  <section class="card card-back">
    <div class="brand">
      <span class="brand-mark"></span>
      <span class="brand-name">Fernvale</span>
    </div>

    <div class="photo-frame" role="img" aria-label="Portrait photo of the sales person"></div>

    <div class="person">
      <p class="person-name">Jordan Hale</p>
      <p class="person-role">Owner</p>
    </div>
    <div class="divider"></div>

    <ul class="contacts">
      <li class="contact">
        <svg viewBox="0 0 26 26"><circle cx="13" cy="13" r="11.5" fill="none" stroke="var(--green)" stroke-width="1.6"/><rect x="9" y="6.5" width="8" height="13" rx="1.5" fill="none" stroke="var(--green)" stroke-width="1.6"/></svg>
        (555) 204-3187
      </li>
      <li class="contact">
        <svg viewBox="0 0 26 26"><circle cx="13" cy="13" r="11.5" fill="none" stroke="var(--green)" stroke-width="1.6"/><rect x="7" y="8.5" width="12" height="9" fill="var(--green)"/><path d="M7 8.5 L13 14 L19 8.5 M7 17.5 L11 13 M19 17.5 L15 13" fill="none" stroke="#fff" stroke-width="1.2"/></svg>
        hello@fernvaleblinds.com
      </li>
      <li class="contact">
        <svg viewBox="0 0 26 26"><circle cx="13" cy="13" r="11.5" fill="none" stroke="var(--green)" stroke-width="1.6"/><circle cx="13" cy="13" r="7" fill="var(--green)"/><path d="M6 13 H20 M13 6 V20 M13 6 C9 10 9 16 13 20 M13 6 C17 10 17 16 13 20" fill="none" stroke="#fff" stroke-width="0.9"/></svg>
        www.fernvaleblinds.com
      </li>
    </ul>

    <address class="address">
      PO BOX 48 Willow Lane<br>
      Harbour Road Ashford
    </address>
  </section>
</body>
</html>
```